Brochure design for healthcare software company

We need a tri-fold brochure design for our healthcare software company that provides software and services for clinicians who manage patients who have or may be diagnosed with cancer.

We have an existing web, business card design and trade show booth design and want the ultimate design to be consistent with these. All of the files including stock images are provided.

Target Market(s)

Nurses, Healthcare professionals

Industry/Entity Type

Healthcare

Requirements
Must have
• Design consistent with attached tradeshow booth and business card.

```html
<!DOCTYPE html>
<html lang="en">
<head>
<meta charset="utf-8">
<title>Meridacare Tri-fold Brochure</title>
<link href="https://fonts.googleapis.com/css2?family=Lato:wght@400;700&family=Roboto:wght@400;700;900&family=Roboto+Condensed:wght@400;700&display=swap" rel="stylesheet">
<style>
  :root{
    --blue:#2e4fb8;
    --blue-dark:#1f3a8f;
    --green:#5cb531;
    --ink:#1d1d22;
    --grey:#5a5f68;
    --paper:#ffffff;
    --backdrop:#e6e9ed;
  }
  *{box-sizing:border-box;margin:0;padding:0}
  html,body{width:949px;height:1200px;overflow:hidden}
  body{background:var(--backdrop);position:relative;font-family:"Roboto",Arial,sans-serif;color:var(--ink)}
  .spread{position:absolute;left:135px;width:679px;height:520px;background:var(--paper);overflow:hidden;box-shadow:0 6px 18px rgba(0,0,0,.18)}
  .spread--outside{top:34px}
  .spread--inside{top:630px}
  .spread > svg.art{position:absolute;inset:0;width:100%;height:100%}
  .abs{position:absolute}

  /* outside: back panel */
  .brand-name{left:0;width:226px;top:226px;text-align:center;font:700 17px/1 "Roboto",Arial,sans-serif;letter-spacing:4px;color:var(--blue)}
  .feature{width:96px;text-align:center}
  .feature svg{width:16px;height:16px;display:block;margin:0 auto 3px}
  .feature h3{font:400 7.5px/1.2 "Roboto",Arial,sans-serif;color:var(--ink);margin-bottom:3px}
  .feature p{font:400 5.2px/1.45 "Roboto",Arial,sans-serif;color:var(--grey)}

  /* outside: mailer panel */
  .contact{left:245px;width:150px;top:382px;text-align:center;font:700 9.5px/1.3 "Roboto Condensed",Arial,sans-serif;color:var(--blue)}
  .social{left:304px;top:446px;display:flex;gap:4px}
  .social span{width:14px;height:14px;background:var(--blue);display:block}
  .social span + span{background:#3aa0e8}
  .site{font:700 12px/1 "Roboto Condensed",Arial,sans-serif;color:var(--ink);text-align:center}
  .site--outside{left:245px;width:150px;top:476px}
  .site--inside{left:470px;width:186px;top:480px}

  /* outside: cover */
  .title{left:480px;width:190px;top:46px;text-align:center}
  .title .title-name{font:900 12px/1 "Roboto",Arial,sans-serif;color:var(--ink);letter-spacing:.5px}
  .title .title-main{font:900 26px/1.05 "Roboto",Arial,sans-serif;color:#fff;letter-spacing:.5px}
  .title .title-sub{display:block;margin:1px auto 0;width:150px;background:var(--green);font:700 9px/12px "Roboto",Arial,sans-serif;color:#fff;letter-spacing:5px}

  /* inside */
  .quote{left:280px;width:166px;top:38px;text-align:center;font:700 14px/1.18 "Lato",Arial,sans-serif;color:var(--green)}
  .nav-title{left:469px;top:40px;width:156px;height:15px;background:var(--blue);color:#fff;font:700 8px/15px "Roboto",Arial,sans-serif;padding-left:6px;letter-spacing:.3px}
  .nav-body{left:472px;top:62px;width:184px}
  .nav-body h4{font:400 5.6px/1.2 "Roboto",Arial,sans-serif;color:var(--blue);margin-top:4px}
  .nav-body p{font:700 5px/1.3 "Roboto Condensed",Arial,sans-serif;color:var(--ink)}
  .card-text{font-family:"Roboto",Arial,sans-serif}
</style>
</head>
<body>

<section class="spread spread--outside">
  <svg class="art" viewBox="0 0 679 520">
    <defs>
      <linearGradient id="fold" x1="0" x2="1">
        <stop offset="0" stop-color="#000" stop-opacity=".08"/>
        <stop offset="1" stop-color="#000" stop-opacity="0"/>
      </linearGradient>
      <radialGradient id="tech" cx=".5" cy=".5" r=".6">
        <stop offset="0" stop-color="#5aa0ff"/>
        <stop offset="1" stop-color="#0b2a8a"/>
      </radialGradient>
      <linearGradient id="office" x1="0" y1="0" x2="1" y2="1">
        <stop offset="0" stop-color="#e9d6c4"/>
        <stop offset=".5" stop-color="#8fa6c9"/>
        <stop offset="1" stop-color="#5a6f9a"/>
      </linearGradient>
      <linearGradient id="keys" x1="0" y1="0" x2="1" y2="1">
        <stop offset="0" stop-color="#f2efef"/>
        <stop offset="1" stop-color="#c9c9cf"/>
      </linearGradient>
    </defs>
    <rect width="679" height="520" fill="#fff"/>
    <!-- cover blue field -->
    <path d="M360 0 L679 0 L679 520 L560 520 C540 440 490 380 460 330 C430 280 400 240 360 200 Z" fill="var(--blue)"/>
    <path d="M478 330 C513 390 533 450 543 520" fill="none" stroke="var(--green)" stroke-width="12"/>
    <!-- swoosh: back panel edge down to the right of the contact block -->
    <path d="M130 0 L215 0 C200 100 230 190 300 260 C380 300 440 400 455 520 L430 520 C415 420 370 330 290 290 C190 230 130 120 130 0 Z" fill="var(--blue)"/>
    <path d="M228 0 C213 100 243 185 312 252 C395 292 455 400 470 520" fill="none" stroke="var(--green)" stroke-width="9"/>
    <path d="M241 0 C226 100 256 180 324 245 C410 285 470 400 485 520" fill="none" stroke="#dfe3ea" stroke-width="4"/>
    <!-- fold shading -->
    <rect x="226" width="14" height="520" fill="url(#fold)"/>
    <rect x="453" width="14" height="520" fill="url(#fold)"/>
    <!-- photos -->
    <circle cx="373" cy="146" r="122" fill="#fff"/>
    <circle cx="373" cy="146" r="116" fill="url(#office)" role="img" aria-label="Photo: nurse on the phone at a records desk"/>
    <circle cx="304" cy="86" r="46" fill="#fff"/>
    <circle cx="304" cy="86" r="42" fill="url(#tech)" role="img" aria-label="Image: glowing blue circuit lines"/>
    <circle cx="467" cy="278" r="64" fill="#fff"/>
    <circle cx="467" cy="278" r="60" fill="url(#keys)" role="img" aria-label="Photo: hands typing on a keyboard"/>
  </svg>

  <div class="abs brand-name">MERIDACARE</div>

  <div class="abs feature" style="left:15px;top:270px">
    <svg viewBox="0 0 16 16"><circle cx="8" cy="8" r="6" fill="none" stroke="var(--blue)" stroke-width="1.4"/><path d="M8 4.5V8l2.5 1.5" fill="none" stroke="var(--green)" stroke-width="1.4"/></svg>
    <h3>Tracking</h3>
    <p>Manage patients, barriers to care, referrals and other data to build treatment and survivorship plans in one click.</p>
  </div>
  <div class="abs feature" style="left:122px;top:270px">
    <svg viewBox="0 0 16 16"><circle cx="8" cy="8" r="5.5" fill="none" stroke="var(--blue)" stroke-width="1.4" stroke-dasharray="2.2 1.2"/><circle cx="8" cy="8" r="2" fill="var(--green)"/></svg>
    <h3>Workflow</h3>
    <p>Customize a streamlined workflow that removes paperwork, reduces data entry and lets you focus on your patients.</p>
  </div>
  <div class="abs feature" style="left:68px;top:333px">
    <svg viewBox="0 0 16 16"><path d="M4 12h8.5a2.8 2.8 0 0 0 0-5.6A4 4 0 0 0 4.6 7 2.5 2.5 0 0 0 4 12z" fill="var(--blue)"/><circle cx="8" cy="14" r="1.4" fill="var(--green)"/></svg>
    <h3>Connected</h3>
    <p>Connects to your existing systems to remove duplicate entry, improve data accuracy and share information across your facilities.</p>
  </div>
  <div class="abs feature" style="left:15px;top:432px">
    <svg viewBox="0 0 16 16"><path d="M2 2v12h12" fill="none" stroke="var(--ink)" stroke-width="1.2"/><path d="M4 11l3-4 3 2 4-5" fill="none" stroke="var(--blue)" stroke-width="1.4"/></svg>
    <h3>Reporting</h3>
    <p>View advanced reports and analytics to gain insight into the state of your facilities, staff and patients.</p>
  </div>
  <div class="abs feature" style="left:122px;top:432px">
    <svg viewBox="0 0 16 16"><path d="M8 1.5l5.5 2v4.2c0 3.3-2.4 5.8-5.5 6.8-3.1-1-5.5-3.5-5.5-6.8V3.5z" fill="var(--green)"/><path d="M5.5 8l2 2 3.2-3.6" fill="none" stroke="#fff" stroke-width="1.3"/></svg>
    <h3>Security</h3>
    <p>Built from the ground up with the latest security and encryption to protect your patients' privacy.</p>
  </div>

  <div class="abs contact">
    MERIDACARE<br>
    (555) 014-2290<br>
    SUPPORT@MERIDACARE.COM<br>
    SALES@MERIDACARE.COM
  </div>
  <div class="abs social" aria-label="Social links"><span></span><span></span></div>
  <div class="abs site site--outside">MERIDACARE.COM</div>

  <div class="abs title">
    <div class="title-name">MERIDACARE</div>
    <div class="title-main">BUSINESS</div>
    <span class="title-sub">BROCHURE</span>
  </div>
</section>

<section class="spread spread--inside">
  <svg class="art" viewBox="0 0 679 520">
    <defs>
      <linearGradient id="fold2" x1="0" x2="1">
        <stop offset="0" stop-color="#000" stop-opacity=".08"/>
        <stop offset="1" stop-color="#000" stop-opacity="0"/>
      </linearGradient>
      <linearGradient id="hands" x1="0" y1="0" x2="1" y2="1">
        <stop offset="0" stop-color="#d7dde6"/>
        <stop offset="1" stop-color="#c49a84"/>
      </linearGradient>
      <linearGradient id="clinic" x1="0" y1="0" x2="1" y2="1">
        <stop offset="0" stop-color="#cfdde4"/>
        <stop offset=".6" stop-color="#b08a74"/>
        <stop offset="1" stop-color="#f1f1f1"/>
      </linearGradient>
      <radialGradient id="lock" cx=".5" cy=".5" r=".6">
        <stop offset="0" stop-color="#4fa3ff"/>
        <stop offset="1" stop-color="#0a2270"/>
      </radialGradient>
      <linearGradient id="tablet" x1="0" y1="0" x2="1" y2="1">
        <stop offset="0" stop-color="#eef3fb"/>
        <stop offset="1" stop-color="#9fb8e6"/>
      </linearGradient>
    </defs>
    <rect width="679" height="520" fill="#fff"/>
    <rect width="453" height="520" fill="var(--green)"/>
    <path d="M240 0 L453 0 L453 175 C360 175 280 115 240 0 Z" fill="#fff"/>
    <path d="M185 0 L232 0 C262 100 340 170 453 185 L453 235 C320 220 210 140 185 0 Z" fill="var(--blue)"/>
    <path d="M453 175 C360 175 280 115 240 0" fill="none" stroke="#dfe3ea" stroke-width="3"/>
    <path d="M0 330 C120 300 220 360 300 420 C360 465 410 480 453 470 L453 505 C400 515 340 495 285 450 C210 395 110 345 0 365 Z" fill="#fff"/>
    <path d="M0 430 C80 420 150 460 190 520 L0 520 Z" fill="var(--blue)"/>
    <rect x="226" width="14" height="520" fill="url(#fold2)"/>
    <rect x="453" width="14" height="520" fill="url(#fold2)"/>
    <circle cx="169" cy="222" r="77" fill="#fff"/>
    <circle cx="169" cy="222" r="72" fill="url(#hands)" role="img" aria-label="Photo: caregiver holding a patient's hands"/>
    <circle cx="269" cy="330" r="113" fill="#fff"/>
    <circle cx="269" cy="330" r="108" fill="url(#clinic)" role="img" aria-label="Photo: smiling clinician at a desk"/>
    <circle cx="419" cy="402" r="54" fill="#fff"/>
    <circle cx="419" cy="402" r="50" fill="url(#lock)" role="img" aria-label="Image: digital padlock security graphic"/>
    <g transform="translate(-4 368) rotate(-14)">
      <rect width="205" height="118" fill="#fff"/>
      <path d="M0 70 C60 55 130 62 205 48 L205 118 L0 118 Z" fill="var(--blue)"/>
      <path d="M0 70 C60 55 130 62 205 48" fill="none" stroke="var(--green)" stroke-width="6"/>
      <text x="190" y="32" text-anchor="end" class="card-text" font-size="11" fill="#555">Dana Holloway</text>
      <text x="185" y="80" text-anchor="end" class="card-text" font-size="6" fill="#fff">555.014.7731</text>
      <text x="185" y="90" text-anchor="end" class="card-text" font-size="6" fill="#fff">555.014.2290</text>
      <text x="185" y="100" text-anchor="end" class="card-text" font-size="6" fill="#fff">dholloway@meridacare.com</text>
    </g>
    <rect x="520" y="410" width="100" height="52" rx="4" fill="url(#tablet)" role="img" aria-label="Illustration: tablet showing analytics charts"/>
    <g fill="var(--blue)">
      <rect x="540" y="436" width="6" height="16"/>
      <rect x="550" y="428" width="6" height="24"/>
      <rect x="560" y="440" width="6" height="12"/>
      <rect x="570" y="424" width="6" height="28"/>
    </g>
  </svg>

  <div class="abs quote">“Streamlining your oncology patient navigation workflow to reach optimal outcomes for your patients.”</div>

  <div class="abs nav-title">MERIDACARE NAVIGATION</div>
  <div class="abs nav-body">
    <h4>Simplified Navigation</h4>
    <p>Track all of your patients from their entry point, for example an abnormal screening exam or a positive diagnosis, through survivorship. Meridacare Navigation allows you to easily maintain a record of all referrals, exams, treatments, contacts, appointments and notes for your patients.</p>
    <h4>Advanced Workflow Tools</h4>
    <p>View and manage your entire patient load in a single dynamic work list area. Completely customizable to match your workflow. Create checklists for every step of your workflow to maintain consistent patient care and monitoring.</p>
    <h4>Reporting and Analytics</h4>
    <p>Quickly demonstrate the value of your navigation efforts with deep analytics and reporting. View current and historical trends for any or all of your facilities and staff, including detailed reporting on work loads, time to care, patient barriers, referrals and appointments.</p>
    <h4>Eliminate Paper</h4>
    <p>Manage all of your paperwork and patient forms in one easy to use area. Automatically create document packets and auto fill forms for patients or referrals with a single click.</p>
    <h4>Integrated</h4>
    <p>Reduce double data entry by integrating the systems you already have. Patients can be seamlessly added and updated without manual efforts.</p>
    <h4>Secure</h4>
    <p>Built from the ground up with security in mind, Meridacare Navigation is completely HIPAA compliant. Rest assured that your and your patients data is protected.</p>
    <h4>Affordable</h4>
    <p>Meridacare Navigation is completely free for an unlimited number of users and facilities. Additional services including deployments, training, secure hosting and workflow consultations are available.</p>
  </div>

  <div class="abs site site--inside">MERIDACARE.COM</div>
</section>

</body>
</html>
```